デザインは年配の方にも読みやすい落ち着いたものを希望します。
今回のイメージと、前回のチラシデータを添付しています。前回は「A4両面カラー」で2種類(添付資料のA・B)制作しましたが、今回は「A3中折カラー」の4ページ1種類にします。前回チラシのaiデータは当選者決定後にお渡し可能です。

デザインは自由にご提案ください。今回のイメージを伝えるために「構成と内容」という資料を添付していますが、このイメージを整えた案でも、内容をふまえてレイアウトを一新した案でも構いません。

文章と写真は弊社で用意します。今回はコピーやコーナー名、レイアウトを中心としたラフデザイン案を募集します。ページ構成と必要な要素は『記載項目』をご覧ください(あわせて添付資料「構成と内容」をご覧ください)。
■1ページ目:表紙
①タイトル ★タイトルはより印象的なものを提案いただきたいです★
②福岡県の地図に約100の蔵元のロゴをレイアウトした図柄(荷印一覧、添付資料「A_表」と概ね同じ)
③しょうゆ県ふくおかの文章(添付資料「B_瓦版」の文章を要約したもの)
④寄稿文(新規)
※文字サイズは添付資料「B_瓦版」の本文サイズ程度を想定しています。ただし、用意する文字量にあわせて調整いただくことがあります。
■2ページ目:しょうゆ製造者一覧(添付資料「A_裏」と概ね同じ)
○蔵元の名前・住所(今回は市区町村まで番地不要)・電話番号をリストで掲載。
■3ページ目:「原料・発酵・熟成・製法・特徴・種類・用法・効果」の説明
レイアウトは自由に提案してください。しょうゆに関する8つのキーワードを説明します。添付資料「構成と内容」では丸を並べたレイアウトですが、これに従う必要はありません。もちろんこのイメージを踏襲したレイアウトでも結構です。
■4ページ目:しょうゆを生かした料理レシピ
○料理レシピ(料理名+写真+特徴説明文+レシピ文)を6種類。添付資料「B_郷土料理」に近いイメージですが、料理は変更になります。
提案時は、A4サイズ4ページ、A3サイズ裏表(2ページ)どちらの形式でも構いません。
当選の方には今回PDFで添付している「A_表・裏、B_郷土料理・瓦版」のaiデータはお渡し可能です。

表紙のインパクトを重視してこの案を選定しました。

短い応募期間でしたが、たくさんのご提案をいただき誠にありがとうございます。
多彩な提案をいただいており、クライアントとしても最後まで選定に迷ったようです。結果として1案選定しますが、ご提案いただいた皆さまに感謝申し上げます。
今後、また機会がありましたらぜひよろしくお願いいたします。

```html
<!DOCTYPE html>
<html lang="ja">
<head>
<meta charset="utf-8">
<title>日本一のしょうゆ県 福岡</title>
<link href="https://fonts.googleapis.com/css2?family=Noto+Serif+JP:wght@400;600;700;900&family=Noto+Sans+JP:wght@400;700&display=swap" rel="stylesheet">
<style>
:root{
  --green:#1f4a36;
  --paper:#efe9dc;
  --paper-shade:#ddd5c2;
  --ink:#1a1a1a;
  --white:#f7f5ef;
  --yellow:#f2d64b;
  --citrus:#e9e14a;
  --rose:#b8325a;
  --map-a:#cfc6b0;
  --map-b:#b9ad90;
  --pot-a:#6b4a33;
  --pot-b:#2a1d14;
}
*{margin:0;padding:0;box-sizing:border-box}
html,body{width:849px;height:1200px;overflow:hidden;background:var(--green)}
.cover{position:relative;width:849px;height:1200px;background:var(--green);font-family:"Noto Serif JP",serif;color:var(--white)}
.paper{position:absolute;left:196px;top:10px;width:457px;height:380px;background:var(--paper)}
.map-art{position:absolute;left:215px;top:30px;width:300px;height:350px;background:radial-gradient(ellipse at 50% 45%,var(--map-a),var(--map-b));border-radius:40% 55% 45% 50%/45% 40% 60% 55%}
.title-box{position:absolute;left:14px;top:12px;width:176px;padding:6px 10px;background:var(--white);color:var(--ink);font-weight:900;font-size:26px;line-height:1.3;white-space:nowrap}
.title-box .big{font-size:30px}
.title-box .small{font-size:22px}
.title-place{position:absolute;left:528px;top:90px;writing-mode:vertical-rl;font-size:110px;font-weight:900;color:var(--ink);line-height:1}
.brush{position:absolute;left:655px;top:120px;width:8px;height:200px;background:var(--rose);border-radius:4px;transform:rotate(3deg)}
.intro{position:absolute;left:14px;top:112px;width:176px;height:196px;writing-mode:vertical-rl;font-size:15px;font-weight:600;line-height:2.5;color:var(--white);padding:4px 6px}
.pot-photo{position:absolute;left:14px;top:425px;width:200px;height:210px;background:linear-gradient(160deg,var(--pot-a),var(--pot-b))}
.letters{position:absolute;left:14px;top:656px;width:212px;height:534px;background:var(--paper);padding:14px 12px;color:var(--ink)}
.letters h2{font-size:22px;font-weight:700;margin-bottom:14px;border-bottom:2px solid var(--green);padding-bottom:4px}
.letters li{list-style:none;background:var(--white);border:1px solid var(--paper-shade);font-family:"Noto Sans JP",sans-serif;font-size:13px;white-space:nowrap;padding:28px 6px;margin-bottom:14px;height:78px}
.headline{position:absolute;top:430px;writing-mode:vertical-rl;font-weight:700;font-size:38px;line-height:1.2;color:var(--white)}
.headline.main{left:760px}
.headline.sub{left:700px;top:470px;font-size:34px}
.column-block{position:absolute;left:285px;width:395px;display:flex;flex-direction:row-reverse;gap:10px}
.column-block.first{top:425px;height:295px}
.column-block.second{top:752px;height:438px}
.column-head{writing-mode:vertical-rl;color:var(--yellow);font-weight:700;font-size:17px;line-height:1.35}
.column-body{writing-mode:vertical-rl;font-size:12.5px;line-height:1.75;color:var(--white);height:100%;flex:1;overflow:hidden}
.rule{position:absolute;left:285px;top:736px;width:395px;height:1px;background:var(--white)}
.citrus{position:absolute;border-radius:50%;background:var(--citrus)}
</style>
</head>
<body>
<main class="cover">
  <div class="paper"></div>
  <div class="map-art" role="img" aria-label="福岡県の地図に約100の蔵元の荷印を配した図柄"></div>
  <div class="title-box">日本一の<br><span class="big">しょうゆ</span><span class="small">県</span></div>
  <h1 class="title-place">福岡</h1>
  <div class="brush"></div>

  <p class="intro">福岡は醤油事業者数日本一。<br>地域に根差した醤油が息づく<br>日本一のしょうゆ県です。</p>

  <div class="pot-photo" role="img" aria-label="しょうゆ差しと器の写真"></div>

  <section class="letters">
    <h2>寄稿文</h2>
    <ul>
      <li>福岡県に初めて行きました。</li>
      <li>福岡県に初めて行きました。</li>
      <li>福岡県に初めて行きました。</li>
      <li>福岡県に初めて行きました。</li>
      <li>福岡県に初めて行きました。</li>
    </ul>
  </section>

  <h2 class="headline main">「しょうゆ県」ふくおか。</h2>
  <p class="headline sub">〜食の都は地醤油の宝庫〜</p>

  <section class="column-block first">
    <h3 class="column-head">和食がユネスコ<br>世界無形文化遺産</h3>
    <p class="column-body">二〇一三年、和食が日本の伝統的な食文化として登録されました。四季の恵みを生かす和食の味わいを、しょうゆが静かに支えています。二〇一三年、和食が日本の伝統的な食文化として登録されました。四季の恵みを生かす和食の味わいを、しょうゆが静かに支えています。二〇一三年、和食が日本の伝統的な食文化として登録されました。四季の恵みを生かす和食の味わいを、しょうゆが静かに支えています。二〇一三年、和食が日本の伝統的な食文化として登録されました。</p>
  </section>

  <div class="rule"></div>

  <section class="column-block second">
    <h3 class="column-head">和食文化の魅力〜味つけ<br>しょうゆとだしの相乗効果</h3>
    <p class="column-body">しょうゆとだしを合わせると、うま味がいっそう深まります。土地ごとの地醤油が、家庭の味と郷土の料理を育ててきました。しょうゆとだしを合わせると、うま味がいっそう深まります。土地ごとの地醤油が、家庭の味と郷土の料理を育ててきました。しょうゆとだしを合わせると、うま味がいっそう深まります。土地ごとの地醤油が、家庭の味と郷土の料理を育ててきました。しょうゆとだしを合わせると、うま味がいっそう深まります。土地ごとの地醤油が、家庭の味と郷土の料理を育ててきました。</p>
  </section>

  <div class="citrus" style="left:200px;top:16px;width:28px;height:28px"></div>
  <div class="citrus" style="left:460px;top:330px;width:24px;height:24px"></div>
  <div class="citrus" style="left:600px;top:30px;width:26px;height:26px"></div>
  <div class="citrus" style="left:100px;top:615px;width:26px;height:26px"></div>
  <div class="citrus" style="left:735px;top:385px;width:26px;height:26px"></div>
  <div class="citrus" style="left:770px;top:955px;width:28px;height:28px"></div>
</main>
</body>
</html>
```